Shaping Lattice Engineering

We need to design the look and feel for an innovation company with software products for solving complex IT problems following socio-technical theory thinking. The company is heavy in designing of complex systems (like an architect shop). The new design will form the foundation of our brand moving forward. We will approach software projects as if one is building a skyscraper or a bridge. We want to humanize technology and not the other way around. Our target groups will be healthcare and the environment. We will be able to take complex problems and turn them into amazing IT solutions that improve the quality of life for people.

Here are more fragments of ideas that can help:
===============

Motivation

The technology described in the application, coincides with “Steer-Via-Pulse” concept of Lorne Vistrup, which suggests managing a business by managing an informational representation of it : Lorne had the following vision:

"Imagine an enterprise design model that defines the behavior of an entire business. Imagine making this model a part of the corporate informational infrastructure, implementing it on technology that connects all relevant sources and users of information and affords maximum sharing among all parts of the firm. Managers could respond to the read-outs appearing on the console, modifying the flight plan en route based on changes in external conditions, monitoring the performance of delegated responsibilities, sending coordinated directions to subsidiary functions, and experiencing exhilaration upon their execution. It constitutes institutional memory and intelligence, which augment management's ability to run the business”.

This product does what Mr. Vistrup envisioned.

The Objective

QTV offers software products for the specification, construction, assembly, and ongoing management of a digital representation that is an exact mirror image of an enterprise. The main idea is the capability of managing the enterprise by managing an information technology representation of it through software. The idea is to manage the enterprise as a total system involving all aspects of operations. That makes the enterprise and all its information technology representation is inseparable. The implication is that the management of change at the business and IT infrastructure levels are unified. For example, by reconfiguring the information representation of the enterprise one can change business performance. By changing the configuration of the business representation one can actually change the organization’s ability to respond to internal and external events. Management leadership can act with the aid of technology to better respond and improve their ability to guide the organization. The knowledge management feature of the digital representation of the enterprise enables managers to monitor the impact of change and therefore help management assess risk and determine whether mitigating responses are necessary.

The technology and product defines a new approach for the design, implementation, and ongoing execution of software systems that are truly business-like rather than applications and workflows.

Software

```html
<!DOCTYPE html>
<html lang="en">
<head>
<meta charset="utf-8">
<title>Marrowfield Systems – Shaping Lattice Engineering</title>
<link rel="stylesheet" href="https://fonts.googleapis.com/css2?family=Open+Sans:wght@300;400&family=Ubuntu+Condensed&family=Ubuntu:wght@500&display=swap">
<style>
:root{
  --teal:#1e9ab5;
  --red:#a5262b;
  --footer:#202020;
  --footer-link:#2d9fc0;
  --body-text:#333;
  --rule:#bbb;
  --header-text:#e6e6e6;
  --header-sub:#9aa3a6;
}
*{margin:0;padding:0;box-sizing:border-box}
html,body{width:1200px;height:1200px;overflow:hidden;background:var(--footer)}
body{font-family:Arial,Helvetica,sans-serif;color:var(--body-text);position:relative}
a{text-decoration:none;color:inherit}

.site-header{position:absolute;top:0;left:0;width:1200px;height:86px;background:linear-gradient(#3a3a3a,#111 60%,#000)}
.brand{position:absolute;left:118px;top:16px}
.brand-name{font-family:'Open Sans',sans-serif;font-weight:400;font-size:28px;color:var(--header-text);line-height:34px}
.brand-tagline{font-family:'Open Sans',sans-serif;font-weight:400;font-size:13px;color:var(--header-sub);line-height:18px}
.utility-links{position:absolute;right:121px;top:51px;font-size:11px;color:var(--teal)}
.utility-links span{color:#aaa;margin:0 4px}

.main-nav{position:absolute;top:86px;left:0;width:1200px;height:41px;background:linear-gradient(#fff,#e8e8e8 60%,#d8d8d8);display:flex;padding-left:110px}
.main-nav a{width:140px;height:41px;line-height:39px;text-align:center;font-family:'Ubuntu Condensed','Arial Narrow',sans-serif;font-size:14px;color:#222;border-right:1px solid #ccc}
.main-nav a.active{width:134px;background:linear-gradient(#1c86a0,#0c5d70);color:#fff}
.main-nav a:last-child{border-right:none}
.nav-rule{position:absolute;top:127px;left:0;width:1200px;height:6px;background:#000}

.hero{position:absolute;top:133px;left:0;width:1200px;height:437px;background:linear-gradient(90deg,#0e3a44,#1b5562 50%,#0e3a44)}
.hero-visual{position:absolute;left:63px;top:0;width:1070px;height:435px;background:radial-gradient(ellipse at 62% 40%,#c9e4ec 0%,#8bb9c6 35%,#4a8292 75%,#2f6473 100%)}
.hero-arrow{position:absolute;top:186px;width:60px;height:60px}
.hero-arrow.prev{left:113px}
.hero-arrow.next{left:1028px}

.banner{position:absolute;top:570px;left:0;width:1200px;height:50px;background:linear-gradient(#5aa3b7,#3f8aa0);border-top:1px solid #2d6f80;border-bottom:1px solid #2d6f80}
.banner-title{position:absolute;left:318px;top:9px;font-family:'Open Sans',sans-serif;font-weight:300;font-size:23px;color:#fff}
.inquire-btn{position:absolute;left:912px;top:7px;width:159px;height:35px;border-radius:5px;background:linear-gradient(#fff,#dde3e5);font-family:'Ubuntu',sans-serif;font-weight:500;font-size:14px;color:#333;line-height:33px;padding-left:22px}
.inquire-btn svg{position:absolute;right:12px;top:12px}

.content{position:absolute;top:620px;left:0;width:1200px;height:394px;background:#fff}
.col-title{font-family:'Open Sans',sans-serif;font-weight:300;font-size:27px;color:#222;position:absolute;top:32px}
.divider{position:absolute;top:40px;width:1px;height:311px;background:var(--rule)}

.service{position:absolute;left:128px;width:270px;height:60px}
.service-icon{position:absolute;left:0;top:4px;width:50px;height:38px;border-radius:4px}
.service h3{position:absolute;left:58px;top:0;font-size:14px;font-weight:bold;color:var(--teal);white-space:nowrap}
.service p{position:absolute;left:58px;top:19px;font-size:12px;line-height:14px;width:210px;color:#333}

.reason{position:absolute;left:455px;width:290px}
.reason h3{font-family:'Open Sans',sans-serif;font-weight:300;font-size:22px;color:var(--teal);line-height:26px}
.reason p{font-size:12px;line-height:14px;color:#333}
.reason a{font-size:11px;color:var(--red);text-decoration:underline}

.about{position:absolute;left:797px;top:90px;width:270px;font-size:12px;line-height:14.5px;color:#333}
.about p{margin-bottom:13px}
.about .more{font-family:'Open Sans',sans-serif;font-size:16px;color:var(--red)}

.site-footer{position:absolute;top:1014px;left:0;width:1200px;height:186px;background:var(--footer)}
.footer-brand{position:absolute;left:138px;top:32px;font-family:'Open Sans',sans-serif;font-weight:400;font-size:18px;color:#fff}
.copyright{position:absolute;left:140px;top:65px;font-size:11px;color:#ddd}
.footer-col{position:absolute;top:30px}
.footer-col h4{font-family:'Ubuntu Condensed','Arial Narrow',sans-serif;font-weight:normal;font-size:17px;color:#fff;margin-bottom:12px}
.footer-col ul{list-style:none}
.footer-col li{font-size:12px;color:var(--footer-link);line-height:22px;padding-left:12px;position:relative;letter-spacing:0.3px}
.footer-col li::before{content:"";position:absolute;left:0;top:8px;border-left:4px solid #ddd;border-top:3px solid transparent;border-bottom:3px solid transparent}
.email-field{position:absolute;left:859px;top:61px;width:185px;height:26px;border:1px solid #555;border-radius:3px;background:#1a1a1a;font-size:12px;color:#999;line-height:24px;padding-left:15px}
.subscribe-btn{position:absolute;left:968px;top:99px;width:81px;height:27px;border-radius:5px;background:linear-gradient(#2aa6c6,#137e9a);font-family:'Ubuntu Condensed','Arial Narrow',sans-serif;font-size:12px;color:#fff;text-align:center;line-height:27px;white-space:nowrap}
</style>
</head>
<body>

<header class="site-header">
  <div class="brand">
    <div class="brand-name">Marrowfield Systems</div>
    <div class="brand-tagline">Shaping Lattice Engineering</div>
  </div>
  <div class="utility-links">Support<span>|</span>FAQs<span>|</span>Site Map<span>|</span>Help</div>
</header>

<nav class="main-nav">
  <a class="active" href="#">Home</a>
  <a href="#">About Us</a>
  <a href="#">Products</a>
  <a href="#">Solutions</a>
  <a href="#">Downloads</a>
  <a href="#">Support</a>
  <a href="#">Contacts</a>
</nav>
<div class="nav-rule"></div>

<section class="hero">
  <div class="hero-visual" role="img" aria-label="Person seen from behind touching a glowing digital interface with charts, world map and cloud network icons"></div>
  <svg class="hero-arrow prev" viewBox="0 0 60 60"><circle cx="30" cy="30" r="27" fill="none" stroke="#fff" stroke-width="4" opacity="0.9"/><path d="M34 17 L21 30 L34 43" fill="none" stroke="#fff" stroke-width="5"/></svg>
  <svg class="hero-arrow next" viewBox="0 0 60 60"><circle cx="30" cy="30" r="27" fill="none" stroke="#fff" stroke-width="4" opacity="0.9"/><path d="M26 17 L39 30 L26 43" fill="none" stroke="#fff" stroke-width="5"/></svg>
</section>

<div class="banner">
  <div class="banner-title">The Best Sofrware in Shaping Lattice Engineering</div>
  <a class="inquire-btn" href="#">inquire service<svg width="8" height="10" viewBox="0 0 8 10"><path d="M2 1 L6 5 L2 9" fill="none" stroke="#333" stroke-width="2"/></svg></a>
</div>

<main class="content">
  <h2 class="col-title" style="left:136px">Services</h2>
  <div class="service" style="top:90px">
    <div class="service-icon" role="img" aria-label="Server hardware icon" style="background:linear-gradient(#ddd,#888 45%,#222 55%,#333)"></div>
    <h3>Lorem ipsum dolor sit amet</h3>
    <p>Sed do eiusmod tempor incididunt ut labore et dolore magna aliqua.</p>
  </div>
  <div class="service" style="top:180px">
    <div class="service-icon" role="img" aria-label="Monitor with cloud download icon" style="background:linear-gradient(#111,#2b2b2b);border:2px solid #444"></div>
    <h3>Lorem ipsum dolor sit amet</h3>
    <p>Sed do eiusmod tempor incididunt ut labore et dolore magna aliqua.</p>
  </div>
  <div class="service" style="top:270px">
    <div class="service-icon" role="img" aria-label="Blue cloud with gear icon" style="background:radial-gradient(ellipse at 50% 40%,#8fe0f5,#2aa6d0 70%);border-radius:20px"></div>
    <h3>Lorem ipsum dolor sit amet</h3>
    <p>Sed do eiusmod tempor incididunt ut labore et dolore magna aliqua.</p>
  </div>

  <div class="divider" style="left:420px"></div>

  <h2 class="col-title" style="left:455px">Why choose us?</h2>
  <div class="reason" style="top:87px">
    <h3>Secure</h3>
    <p>Lorem ipsum dolor sit amet, consectetur adipisicing elit, sed do eiusmod tempor incididunt ut.</p>
    <a href="#">read more</a>
  </div>
  <div class="reason" style="top:170px">
    <h3>Robust</h3>
    <p>Lorem ipsum dolor sit amet, consectetur adipisicing elit, sed do eiusmod tempor incididunt ut.</p>
    <a href="#">read more</a>
  </div>
  <div class="reason" style="top:252px">
    <h3>Interactive</h3>
    <p>Lorem ipsum dolor sit amet, consectetur adipisicing elit, sed do eiusmod tempor incididunt ut.</p>
    <a href="#">read more</a>
  </div>

  <div class="divider" style="left:767px"></div>

  <h2 class="col-title" style="left:797px">Who we are</h2>
  <div class="about">
    <p>Lorem ipsum dolor sit amet, consectetur adipisicing elit, sed do eiusmod tempor incididunt ut labore et dolore magna aliqua. Ut enim ad minim veniam, quis nostrud exercitation ullamco laboris nisi ut aliquip ex ea commodo consequat.</p>
    <p>Duis aute irure dolor in reprehenderit in voluptate velit esse cillum dolore eu fugiat nulla pariatur. Excepteur sint occaecat cupidatat non proident, sunt in culpa qui officia deserunt mollit anim id est laborum</p>
    <a class="more" href="#">read more</a>
  </div>
</main>

<footer class="site-footer">
  <div class="footer-brand">Marrowfield Systems</div>
  <div class="copyright">© Copyright Software 2014</div>

  <div class="footer-col" style="left:339px">
    <h4>Why Us</h4>
    <ul><li>Our Clients</li><li>Technology</li><li>Soft Labs</li></ul>
  </div>
  <div class="footer-col" style="left:459px">
    <h4>Quick Links</h4>
    <ul><li>Lorem ipsum dolor</li><li>Amet consectetuer</li><li>Mauris vel tortor vitae</li><li>Nibh condimentum</li></ul>
  </div>
  <div class="footer-col" style="left:659px">
    <h4>Support</h4>
    <ul><li>Nibh condimentum</li><li>Integer ac lacus</li><li>Sociis natoque</li><li>Enatibus et magnis</li></ul>
  </div>
  <div class="footer-col" style="left:859px">
    <h4>Newsletter:</h4>
  </div>
  <div class="email-field">Enter your email here</div>
  <a class="subscribe-btn" href="#">SUBSCRIBE</a>
</footer>

</body>
</html>
```